Harlow Stonefield Civil Construction website design

We want a Bold website to promote our Heavy Civil Construction company, We would like an organic / tangible feel to the site. The pictures will be over saturated so they pop. We need to be able to easliy upload new projects and pictures on a regular basis.
Home page will have a full screen width image, "home page image" with silhouette and logo. It will also have about us area and picture
Page 2 will be Project Gallery with pictures in project folders
Page 3 will be an employment application form and submission
Page 4 will be Contact Us
Target Market(s)
Construction indusrty
Industry/Entity Type
Contractor
Coding
Coded - Design and coding required
Number of Pages Required
4 page
Font styles to use
Other font styles liked:
- Hypatia Sans Pro Light
Look and feel

```html
<!DOCTYPE html>
<html lang="en">
<head>
<meta charset="utf-8">
<title>Contact Us – Harlow Stonefield Civil Construction</title>
<link rel="stylesheet" href="https://fonts.googleapis.com/css2?family=Montserrat:wght@400;500;600;700&display=swap">
<style>
  :root {
    --ink: #1b1b1b;
    --muted: #6f6f6f;
    --brand-blue: #2a3f9c;
    --accent: #f2c21b;
    --hero: #34476e;
    --map: #5d6f84;
    --rule: #2a2a2a;
    --footer: #121212;
    --white: #ffffff;
  }
  * { box-sizing: border-box; margin: 0; padding: 0; }
  html, body { width: 1200px; height: 2208px; overflow: hidden; }
  body { position: relative; background: var(--white); font-family: "Montserrat", sans-serif; color: var(--ink); }
  .abs { position: absolute; }

  /* header */
  .brand { left: 40px; top: 59px; display: flex; align-items: center; gap: 10px; }
  .brand-mark { width: 36px; height: 36px; border: 3px solid var(--brand-blue); }
  .brand-name { border-left: 1px solid #8a8a8a; padding-left: 7px; }
  .brand-name strong { display: block; color: var(--brand-blue); font-weight: 500; font-size: 17px; letter-spacing: 0.2px; line-height: 18px; }
  .brand-name span { display: block; color: var(--brand-blue); font-weight: 500; font-size: 10px; letter-spacing: 3.1px; line-height: 14px; }
  .main-nav { top: 76px; right: 38px; display: flex; gap: 41px; font-size: 13.5px; font-weight: 500; }
  .main-nav a { color: var(--ink); text-decoration: none; position: relative; }
  .main-nav a.is-active::after { content: ""; position: absolute; left: 0; right: 0; bottom: -6px; height: 2px; background: var(--accent); }
  .main-nav a.is-dim { color: var(--muted); }

  /* hero */
  .hero { left: 38px; top: 172px; width: 1124px; height: 450px; background: linear-gradient(180deg, #4a5d82 0%, var(--hero) 55%, #22335a 100%); }
  .hero h1 { position: absolute; left: 0; right: 0; top: 205px; text-align: center; color: var(--white); font-size: 37px; font-weight: 600; letter-spacing: 2px; }
  .hero-line { position: absolute; left: 561px; top: 330px; width: 2px; height: 120px; background: var(--accent); }

  /* contact details */
  .section-title { left: 116px; top: 764px; font-size: 27px; font-weight: 700; }
  .section-title::after { content: ""; position: absolute; left: 0; top: 45px; width: 38px; height: 2px; background: var(--accent); }
  .intro { left: 116px; top: 840px; width: 420px; font-size: 13.5px; font-weight: 500; line-height: 36px; }
  .company { left: 116px; top: 994px; font-size: 17.5px; font-weight: 600; }
  .address { left: 116px; top: 1049px; font-size: 17px; }
  .email { left: 116px; top: 1102px; font-size: 17px; letter-spacing: 1px; color: var(--ink); text-decoration: none; border-bottom: 2px solid var(--accent); padding-bottom: 1px; }
  .rule { left: 116px; width: 616px; height: 1px; background: var(--rule); }
  .detail { left: 118px; font-size: 17px; letter-spacing: 1px; }
  .detail b { color: var(--accent); font-weight: 500; margin-right: 18px; }

  /* map */
  .map { left: 38px; top: 1421px; width: 1124px; height: 450px; background: linear-gradient(90deg, var(--map) 0%, var(--map) 40%, #6c7a8a 60%, #717e8c 100%); }
  .map p { position: absolute; left: 0; right: 0; top: 205px; text-align: center; color: var(--white); font-size: 22px; font-weight: 600; }
  .zoom { position: absolute; right: 12px; bottom: 12px; width: 23px; height: 56px; background: #f0f0f0; opacity: .55; }

  /* footer */
  .site-footer { left: 0; top: 2020px; width: 1200px; height: 188px; background: var(--footer); }
  .foot-nav { position: absolute; left: 40px; top: 80px; display: flex; gap: 41px; font-size: 13.5px; font-weight: 600; }
  .foot-nav a { color: var(--white); text-decoration: none; }
  .foot-nav a.is-active { color: var(--accent); }
  .follow { position: absolute; left: 882px; top: 79px; color: var(--white); font-size: 13.5px; font-weight: 600; }
  .social { position: absolute; left: 1006px; top: 78px; display: flex; gap: 17px; }
  .social span { width: 17px; height: 17px; background: var(--white); display: block; }
  .social span.is-active { background: var(--accent); }
  .foot-rule { position: absolute; left: 38px; top: 159px; width: 1124px; height: 1px; background: var(--white); }
  .legal { position: absolute; top: 170px; font-size: 9.5px; font-weight: 600; color: #cfcfcf; }
</style>
</head>
<body>
  <header>
    <div class="abs brand">
      <div class="brand-mark"></div>
      <div class="brand-name"><strong>HARLOW STONEFIELD</strong><span>CIVIL CONSTRUCTION</span></div>
    </div>
    <nav class="abs main-nav">
      <a href="#">HOME</a>
      <a href="#">SERVICES</a>
      <a href="#" class="is-active">PROJECTS</a>
      <a href="#">CAREERS</a>
      <a href="#" class="is-dim">CONTACT</a>
    </nav>
  </header>

  <section class="abs hero" role="img" aria-label="Blue-tinted photo of a modern glass lobby with seating">
    <h1>CONTACT US</h1>
    <div class="hero-line"></div>
  </section>

  <h2 class="abs section-title">CONTACT</h2>
  <p class="abs intro">We are ready to provide excellent design and expertise to your upcoming project.</p>
  <h3 class="abs company">HARLOW STONEFIELD CIVIL CONSTRUCTION</h3>
  <p class="abs address">4180 Quarry Ridge Road, Millbrook, FL 34900</p>
  <a class="abs email" href="#">mail@harlowstonefield.com</a>
  <div class="abs rule" style="top:1165px"></div>
  <p class="abs detail" style="top:1191px"><b>TEL</b>555 014 2270</p>
  <div class="abs rule" style="top:1242px"></div>
  <p class="abs detail" style="top:1268px"><b>FAX</b>555 000 0000</p>
  <div class="abs rule" style="top:1319px"></div>

  <section class="abs map" role="img" aria-label="Regional road map with the office location marked">
    <p>Use ctrl + scroll to zoom the map</p>
    <div class="zoom"></div>
  </section>

  <footer class="abs site-footer">
    <nav class="foot-nav">
      <a href="#">HOME</a>
      <a href="#">CAREERS</a>
      <a href="#" class="is-active">CONTACT</a>
    </nav>
    <div class="follow">FOLLOW US</div>
    <div class="social">
      <span></span><span></span><span class="is-active"></span><span></span><span></span>
    </div>
    <div class="foot-rule"></div>
    <p class="legal" style="left:38px">@ HARLOW STONEFIELD Civil Construction 2019 All Rights Reserved</p>
    <p class="legal" style="right:38px">Privacy Policy | Terms &amp; Conditions</p>
  </footer>
</body>
</html>
```